Designer Instructions – Updated Referral Program Flyer

(Based on the mock-up in “Brief Layout and Instructions.pdf”)

OVERALL STYLE + LAYOUT

Maintain the same general layout, structure, and flow as the mock-up flyer (front and back).

This is an update of an older flyer, not a full redesign — keep the same sections, proportions, and overall visual feel, but with cleaner, more modern design improvements.

The final flyer should look clean, bold, professional, and high-impact, geared toward realtors, property managers, and contractors who refer work.

FRONT SIDE INSTRUCTIONS
1. Header Section

Remove the Tallow Ridge Builders logo from the top banner.
(Shown on page 1 of the PDF)

2. Main Headline

Keep the same three-line structure:
EARN
UNLIMITED
CASH

Center it, maximize impact, and increase the font size of CASH so all three words match in importance.

Make the headline bold, clean, and the main focal point.

3. Cash Incentive Box

Keep the "$500 minimum OR 10% per referral" box, but upgrade the graphics to look sharper and more modern.

Ensure the wording matches exactly what’s in the mock-up.

4. Premier Partner Program Ribbon

Clean up and modernize the "PREMIER PARTNER PROGRAM" bar while keeping the same position and structure.

Ensure the checkmark badge remains crisp and professional.

5. Supporting Icons Section

Keep the four icons/benefit boxes (Guaranteed Payout, Free Evaluations, Affordable Solutions, Industry Leaders) in the same order.

Update the icons to cleaner, more modern styles — but maintain the same meanings.

Improve alignment and spacing for sharper visual consistency.

6. Remove Icons in Contact Area

At the bottom (“CALL TEXT OR BOOK ONLINE 555-014-2796 TallowRidgeBuilders.example”), remove the phone and internet icons, as noted on page 2 of the PDF.

7. Replace All Images

I (Darnell) will provide all updated stock images separately via email.

Replace the flood/water-damage imagery and roof leak with the new images I send.

Keep image placement and proportions the same as the mock-up.

BACK SIDE INSTRUCTIONS
1. Header Image + “REFER / EARN” Section

Maintain the same large split-image layout (“The more you refer, the more you earn”).

Replace all background imagery with the new assets I will send.

Keep the CASH FLOW image section but modernize the type and spacing.

2. “HOW IT WORKS” Section

Preserve the three-column layout:

Refer Flood, Water & Mold Damage

We Take Care of Everything (evaluations/insurance)

Get Paid to Share

Update images, tighten spacing, and use modern iconography.

3. Remove Phone/Internet Icons

Same as the front side — remove small communication icons and keep only the text/number/URL.

4. Bottom Contact Bar

Keep the blue bar, same wording, same layout — just modernize the style if needed for clarity.

5. Replace All Back-Side Images

Again, I will email you the image assets.

Keep the layout EXACT — just update with higher-quality photos and improved design.

TEXT CONTENT (Keep as-is unless spacing adjustments needed)

All text shown in the PDF should remain exactly the same unless spacing or visual balance requires minor adjustments.
Example from page 3:

“REFER FLOOD, MOLD & CONSTRUCTION JOBS”

“We Schedule a Free Estimate. If Approved, You Get Paid.”

“Everybody Benefits From Referrals”

Everything stays, just refreshed and visually improved.

DESIGN GOALS

Flyer should look high-end and trustworthy, not salesy.

Consistent color theme: blues, whites, yellows, same palette as original.

Use bold, modern fonts with strong readability.

Ensure all headlines pop and all benefit boxes are clean, well-aligned, and evenly spaced.

The final result should feel like a premium referral program flyer for a top-tier restoration/remodel company.

FILES I WILL PROVIDE

I will send the designer:

All replacement stock photos

Any updated logos (if needed)

Original high-resolution version of the mock-up (if available)

Any additional icons preferred

0054AA
0677BA
7BADD7
CADEEF
E8F1F8

• Designer Instructions – Updated Referral Program Flyer (Based on the mock-up in “Brief Layout and Instructions.pdf”) OVERALL STYLE + LAYOUT Maintain the same general layout, structure, and flow as the mock-up flyer (front and back). This is an update of an older flyer, not a full redesign — keep the same sections, proportions, and overall visual feel, but with cleaner, more modern design improvements. The final flyer should look clean, bold, professional, and high-impact, geared toward realtors, property managers, and contractors who refer work. FRONT SIDE INSTRUCTIONS 1. Header Section Remove the Tallow Ridge Builders logo from the top banner. (Shown on page 1 of the PDF) 2. Main Headline Keep the same three-line structure: EARN UNLIMITED CASH Center it, maximize impact, and increase the font size of CASH so all three words match in importance. Make the headline bold, clean, and the main focal point. 3. Cash Incentive Box Keep the "$500 minimum OR 10% per referral" box, but upgrade the graphics to look sharper and more modern. Ensure the wording matches exactly what’s in the mock-up. 4. Premier Partner Program Ribbon Clean up and modernize the "PREMIER PARTNER PROGRAM" bar while keeping the same position and structure. Ensure the checkmark badge remains crisp and professional. 5. Supporting Icons Section Keep the four icons/benefit boxes (Guaranteed Payout, Free Evaluations, Affordable Solutions, Industry Leaders) in the same order. Update the icons to cleaner, more modern styles — but maintain the same meanings. Improve alignment and spacing for sharper visual consistency. 6. Remove Icons in Contact Area At the bottom (“CALL TEXT OR BOOK ONLINE 555-014-2796 TallowRidgeBuilders.example”), remove the phone and internet icons, as noted on page 2 of the PDF. 7. Replace All Images I (Darnell) will provide all updated stock images separately via email. Replace the flood/water-damage imagery and roof leak with the new images I send. Keep image placement and proportions the same as the mock-up. BACK SIDE INSTRUCTIONS 1. Header Image + “REFER / EARN” Section Maintain the same large split-image layout (“The more you refer, the more you earn”). Replace all background imagery with the new assets I will send. Keep the CASH FLOW image section but modernize the type and spacing. 2. “HOW IT WORKS” Section Preserve the three-column layout: Refer Flood, Water & Mold Damage We Take Care of Everything (evaluations/insurance) Get Paid to Share Update images, tighten spacing, and use modern iconography. 3. Remove Phone/Internet Icons Same as the front side — remove small communication icons and keep only the text/number/URL. 4. Bottom Contact Bar Keep the blue bar, same wording, same layout — just modernize the style if needed for clarity. 5. Replace All Back-Side Images Again, I will email you the image assets. Keep the layout EXACT — just update with higher-quality photos and improved design. TEXT CONTENT (Keep as-is unless spacing adjustments needed) All text shown in the PDF should remain exactly the same unless spacing or visual balance requires minor adjustments. Example from page 3: “REFER FLOOD, MOLD & CONSTRUCTION JOBS” “We Schedule a Free Estimate. If Approved, You Get Paid.” “Everybody Benefits From Referrals” Everything stays, just refreshed and visually improved. DESIGN GOALS Flyer should look high-end and trustworthy, not salesy. Consistent color theme: blues, whites, yellows, same palette as original. Use bold, modern fonts with strong readability. Ensure all headlines pop and all benefit boxes are clean, well-aligned, and evenly spaced. The final result should feel like a premium referral program flyer for a top-tier restoration/remodel company. FILES I WILL PROVIDE I will send the designer: All replacement stock photos Any updated logos (if needed) Original high-resolution version of the mock-up (if available) Any additional icons preferred

```html
<!DOCTYPE html>
<html lang="en">
<head>
<meta charset="utf-8">
<title>Referral Partner Program Flyer – Front and Back</title>
<link href="https://fonts.googleapis.com/css2?family=Bebas+Neue&family=Montserrat:wght@500;600;700;800;900&display=swap" rel="stylesheet">
<style>
  :root{
    --blue:#0a3a9e;
    --blue-deep:#062a7c;
    --navy:#0d1f52;
    --yellow:#ffb800;
    --white:#ffffff;
    --sky:#cadeef;
    --mist:#e8f1f8;
    --page:#ffffff;
  }
  *{box-sizing:border-box;margin:0;padding:0}
  html,body{width:1200px;height:1200px;overflow:hidden;background:var(--page)}
  body{position:relative;font-family:"Montserrat",Arial,sans-serif}
  .card{position:absolute;left:215px;width:770px;height:498px;background:var(--white);overflow:hidden;box-shadow:0 4px 14px rgba(0,0,0,.12)}
  .card--front{top:81px}
  .card--back{top:637px}
  .abs{position:absolute}

  /* front header */
  .hero-photo{left:0;top:0;width:770px;height:200px;
    background:linear-gradient(90deg,#cfe3f2 0%,#eef4f8 22%,#d8dcdf 30%,#f4f5f6 70%,#e6e8ea 85%,#d3d6d9 100%)}
  .headline-panel{left:234px;top:0;width:303px;height:212px;background:var(--blue);border-radius:0 0 34px 34px;text-align:center}
  .headline-earn{top:4px;left:0;width:100%;font-weight:800;font-size:68px;line-height:1;color:var(--white);letter-spacing:1px}
  .headline-unlimited{top:63px;left:0;width:100%;font-weight:800;font-size:34px;line-height:1;color:var(--yellow)}
  .headline-cash{top:92px;left:0;width:100%;font-weight:800;font-size:68px;line-height:1;color:var(--yellow)}
  .flood-pill{left:118px;top:162px;width:535px;height:39px;background:var(--yellow);border:2px solid var(--blue);border-radius:20px;
    font-weight:800;font-size:27px;line-height:35px;color:var(--navy);text-align:center;letter-spacing:.3px}

  /* incentive pills */
  .incentive{top:222px;height:49px;background:var(--blue);border:2px solid var(--yellow);border-radius:25px;
    font-family:"Bebas Neue",Impact,sans-serif;font-size:31px;line-height:47px;color:var(--yellow);text-align:center}
  .incentive--min{left:11px;width:172px}
  .incentive--pct{left:200px;width:228px}
  .incentive-or{left:180px;top:227px;width:39px;height:39px;border-radius:50%;background:var(--yellow);
    font-family:"Montserrat",Arial,sans-serif;font-weight:800;font-size:22px;line-height:36px;color:var(--blue);text-align:center}
  .incentive--premier{left:441px;width:317px}

  .tagline{left:0;width:770px;text-align:center;font-weight:800;color:var(--navy);white-space:nowrap}
  .tagline--partner{top:274px;font-size:26px}
  .tagline--send{top:432px;font-size:24px}
  .tagline--how{top:243px;font-size:27px}
  .tagline--refer{top:420px;font-size:23.5px}

  /* benefit boxes */
  .benefit{position:absolute;background:var(--blue);border:2px solid var(--yellow);border-radius:28px 18px 28px 28px;
    box-shadow:0 6px 6px -3px rgba(0,0,0,.25);color:var(--white)}
  .benefit-title{position:absolute;left:13px;font-weight:700;color:var(--yellow);line-height:1.2;text-transform:uppercase}
  .benefit-rule{position:absolute;left:13px;height:2px;background:var(--yellow)}
  .benefit-text{position:absolute;left:13px;font-weight:500;line-height:1.3}
  .benefit-icon{position:absolute;border-radius:50%;background:var(--white);border:2px solid var(--blue);display:flex;align-items:center;justify-content:center}

  .front-benefit{top:309px;width:180px;height:110px}
  .front-benefit .benefit-title{top:12px;font-size:14px}
  .front-benefit .benefit-rule{top:49px;width:108px}
  .front-benefit .benefit-text{top:57px;font-size:11.5px;width:156px}
  .front-benefit .benefit-icon{right:-8px;top:-9px;width:52px;height:52px}

  .back-step{top:283px;width:245px;height:128px}
  .back-step .benefit-title{top:16px;font-size:13.5px;width:190px}
  .back-step .benefit-rule{top:56px;width:125px}
  .back-step .benefit-text{top:70px;font-size:13.5px;width:215px}
  .back-step .benefit-icon{right:-8px;top:-8px;width:58px;height:58px}

  /* contact bar */
  .contact-bar{left:0;top:458px;width:770px;height:40px;background:var(--blue);font-weight:700;font-size:16px;line-height:40px;white-space:nowrap}
  .contact-cta{position:absolute;left:17px;color:var(--yellow)}
  .contact-phone{position:absolute;left:300px;color:var(--white)}
  .contact-sep{position:absolute;left:437px;color:var(--white)}
  .contact-web{position:absolute;right:14px;color:var(--white);font-size:14.5px}

  /* back header */
  .refer-band{left:0;top:0;width:770px;height:235px;background:linear-gradient(100deg,#0b3aa8 0%,#1246b8 45%,#0d3aa2 100%)}
  .refer-line{left:44px;font-weight:800;line-height:1;white-space:nowrap}
  .refer-small{font-size:37px;color:var(--white)}
  .refer-big{font-size:86px;color:var(--yellow)}
  .money-photo{left:381px;top:0;width:338px;height:235px;
    background:radial-gradient(ellipse 48% 50% at 50% 52%,#eef1ea 0%,#d6ddd2 45%,rgba(196,206,196,.55) 75%,rgba(19,70,184,0) 100%)}
  .cash-flow{left:420px;top:70px;width:270px;text-align:center;font-weight:800;font-size:58px;line-height:.88;color:var(--yellow);
    text-shadow:0 2px 4px rgba(0,0,0,.35)}
</style>
</head>
<body>

<!-- FRONT -->
<section class="card card--front">
  <div class="abs hero-photo" role="img" aria-label="Bright modern remodeled interior: ocean-view living room on the left, white marble kitchen on the right"></div>
  <div class="abs headline-panel">
    <div class="abs headline-earn">EARN</div>
    <div class="abs headline-unlimited">UNLIMITED</div>
    <div class="abs headline-cash">CA$H</div>
  </div>
  <div class="abs flood-pill">GET PAID TO REFER A FLOOD</div>

  <div class="abs incentive incentive--min">$500 MINIMUM</div>
  <div class="abs incentive incentive--pct">&nbsp;&nbsp;10% PER REFERRAL</div>
  <div class="abs incentive-or">or</div>
  <div class="abs incentive incentive--premier">PREMIER PARTNER PROGRAM</div>

  <div class="abs tagline tagline--partner">PARTNER WITH US &amp; EVERYBODY WINS!</div>

  <div class="benefit front-benefit" style="left:11px">
    <div class="benefit-title">Guaranteed<br>Payout*</div>
    <div class="benefit-rule"></div>
    <div class="benefit-text">Minimum $500 or 10% of Total Invoice Paid Fast</div>
    <div class="benefit-icon"><svg width="30" height="30" viewBox="0 0 30 30" fill="none" stroke="#0a3a9e" stroke-width="1.6" stroke-linecap="round" stroke-linejoin="round"><rect x="5" y="4" width="20" height="6" rx="1"/><rect x="9" y="10" width="12" height="16" rx="1"/><path d="M15 13v10M17.5 14.5h-3.5a1.5 1.5 0 0 0 0 3h2a1.5 1.5 0 0 1 0 3h-3.5"/><path d="M3 22v-6l-2 2M3 16l2 2"/></svg></div>
  </div>
  <div class="benefit front-benefit" style="left:200px">
    <div class="benefit-title">Free<br>Estimates</div>
    <div class="benefit-rule"></div>
    <div class="benefit-text">Fast &amp; Free Inspections<br>&amp; Written Estimates</div>
    <div class="benefit-icon"><svg width="30" height="30" viewBox="0 0 30 30" fill="none" stroke="#0a3a9e" stroke-width="1.6" stroke-linecap="round" stroke-linejoin="round"><rect x="5" y="6" width="14" height="20" rx="1.5"/><path d="M8 11h8M8 15h5"/><rect x="14" y="16" width="10" height="11" rx="1"/><path d="M16 19h6M16 22h2M20 22h2M16 25h2M20 25h2"/><circle cx="22" cy="8" r="5"/><path d="M22 5.5V8l1.8 1.2"/></svg></div>
  </div>
  <div class="benefit front-benefit" style="left:389px">
    <div class="benefit-title">Affordable<br>Solutions</div>
    <div class="benefit-rule"></div>
    <div class="benefit-text">Lowest Out of Pocket<br>Costs for Your Customers</div>
    <div class="benefit-icon"><svg width="30" height="30" viewBox="0 0 30 30" fill="none" stroke="#0a3a9e" stroke-width="1.6" stroke-linecap="round" stroke-linejoin="round"><path d="M15 5a5 5 0 0 0-3 9v2h6v-2a5 5 0 0 0-3-9z"/><path d="M13 18h4M15 1v1.5M8 4l1 1M22 4l-1 1"/><path d="M3 22h6l4 2h5a1.5 1.5 0 0 0 0-3h-4M18 22l6-3a1.5 1.5 0 0 1 2 2l-8 5H3"/></svg></div>
  </div>
  <div class="benefit front-benefit" style="left:578px">
    <div class="benefit-title">Industry<br>Leaders</div>
    <div class="benefit-rule"></div>
    <div class="benefit-text">Licensed &amp; Certified<br>Experts &nbsp;Provide 100%<br>Guarantee</div>
    <div class="benefit-icon"><svg width="30" height="30" viewBox="0 0 30 30" fill="none" stroke="#0a3a9e" stroke-width="1.6" stroke-linecap="round" stroke-linejoin="round"><circle cx="15" cy="9" r="2.5"/><path d="M11 24v-8a4 4 0 0 1 8 0v8"/><circle cx="7" cy="13" r="2"/><path d="M4 24v-5a3 3 0 0 1 6 0"/><circle cx="23" cy="13" r="2"/><path d="M20 19a3 3 0 0 1 6 0v5"/><path d="M15 2l.7 1.4 1.5.2-1.1 1 .3 1.5-1.4-.7-1.4.7.3-1.5-1.1-1 1.5-.2z"/></svg></div>
  </div>

  <div class="abs tagline tagline--send">SEND REFERRALS. GET PAID. GROW YOUR BUSINESS</div>

  <div class="abs contact-bar">
    <span class="contact-cta">CALL, TEXT OR BOOK ONLINE</span>
    <span class="contact-phone">555-014-2796</span>
    <span class="contact-sep">|</span>
    <span class="contact-web">www.TallowRidgeBuilders.example</span>
  </div>
</section>

<!-- BACK -->
<section class="card card--back">
  <div class="abs refer-band" role="img" aria-label="Modern interior photo with a deep blue color overlay"></div>
  <div class="abs refer-line refer-small" style="top:10px">THE MORE YOU</div>
  <div class="abs refer-line refer-big" style="top:42px">REFER</div>
  <div class="abs refer-line refer-small" style="top:118px">THE MORE YOU</div>
  <div class="abs refer-line refer-big" style="top:146px;font-size:92px;letter-spacing:-1px">EARN</div>
  <div class="abs money-photo" role="img" aria-label="Fan of hundred-dollar bills held in a hand"></div>
  <div class="abs cash-flow">CASH<br>FLOW</div>

  <div class="abs tagline tagline--how">HOW IT WORKS</div>

  <div class="benefit back-step" style="left:5px">
    <div class="benefit-title">Refer Flood, Mold<br>&amp; Construction Jobs:</div>
    <div class="benefit-rule"></div>
    <div class="benefit-text">It’s Simple to Refer 24/7: Call, Text or Book Online.</div>
    <div class="benefit-icon"><svg width="34" height="34" viewBox="0 0 34 34" fill="none" stroke="#0d1f52" stroke-width="1.5" stroke-linecap="round" stroke-linejoin="round"><circle cx="17" cy="17" r="7"/><circle cx="17" cy="15" r="2"/><path d="M13.5 21a3.5 3.5 0 0 1 7 0"/><circle cx="6" cy="6" r="3"/><circle cx="28" cy="6" r="3"/><circle cx="6" cy="28" r="3"/><circle cx="28" cy="28" r="3"/><path d="M8.5 8.5l3 3M25.5 8.5l-3 3M8.5 25.5l3-3M25.5 25.5l-3-3"/></svg></div>
  </div>
  <div class="benefit back-step" style="left:261px">
    <div class="benefit-title">We Take Care<br>of Everything:</div>
    <div class="benefit-rule"></div>
    <div class="benefit-text">We Schedule a Free Estimate. If Approved, You Get Paid.</div>
    <div class="benefit-icon"><svg width="34" height="34" viewBox="0 0 34 34" fill="none" stroke="#0d1f52" stroke-width="1.5" stroke-linecap="round" stroke-linejoin="round"><circle cx="12" cy="7" r="2.5"/><circle cx="22" cy="7" r="2.5"/><path d="M8 16a4 4 0 0 1 8 0M18 16a4 4 0 0 1 8 0"/><path d="M17 25l-4-4a2.2 2.2 0 0 1 4-2 2.2 2.2 0 0 1 4 2z"/><path d="M3 18l4 8h6M31 18l-4 8h-6"/></svg></div>
  </div>
  <div class="benefit back-step" style="left:518px">
    <div class="benefit-title">Everybody Benefits<br>From Referrals</div>
    <div class="benefit-rule"></div>
    <div class="benefit-text">We Provide Expert Quality Work for Affordable Price.</div>
    <div class="benefit-icon"><svg width="34" height="34" viewBox="0 0 34 34" fill="none" stroke="#0d1f52" stroke-width="1.5" stroke-linecap="round" stroke-linejoin="round"><circle cx="17" cy="12" r="6"/><path d="M19 9.5h-2.8a1.3 1.3 0 0 0 0 2.6h1.6a1.3 1.3 0 0 1 0 2.6H15M17 8v8.5"/><path d="M3 18l5 9h6v-4l-4-4M31 18l-5 9h-6v-4l4-4"/><path d="M17 2v1M9 5l1 1M25 5l-1 1"/></svg></div>
  </div>

  <div class="abs tagline tagline--refer">REFER: FLOODS, REMODELS, RENOVATIONS &amp; REPAIRS</div>

  <div class="abs contact-bar">
    <span class="contact-cta">CALL, TEXT OR BOOK ONLINE</span>
    <span class="contact-phone">555-014-2796</span>
    <span class="contact-sep">|</span>
    <span class="contact-web">www.TallowRidgeBuilders.example</span>
  </div>
</section>

</body>
</html>
```